Gutschein-Design für Lorenzo Restaurant
Zielgruppe
Pizzeria Restaurant à la carte/ Das Design soll Jedem gefallen, mir, Familien, Pärchen, etc.
Aufgabenstellung
Die Gutscheine werden von unserem Kassensystem bedruckt. Die Größe ist ca. 95 mm/ 80 mm. Dieser Bon sollte in die Gutschein-Hülle, die ich jetzt brauche eingesteckt sein. Die Masse sollen 105x105 mm sein, offen 105x210 mm .
Text:
Auf Seite 1:
- Das Logo
- Geschenk-Gutschein
Auf Seite 2:
- Der Gutschein kann für Vieles gut sein
- In unserem Fall lässt unsere reichhaltige Karte viele Möglichkeiten offen
- Auf jeden Fall wird bestimmt geschlemmt, geschmaust und genossen
- Wir wünschen guten Appetit
Auf Seite 3 für die Druckerei:
- 2 Halbkreise gestanzt und 1x gerillt, rundum auf Endformat beschnitten.
- 1-Bruch Falz
Hier gehört der Gutschein-Bon 95/80 mm eingesteckt
Auf Seite 4:
Lorenzo
Restaurantbetriebsgesellschaft m.b.H.
www.lorenzo-trattoria.at
Im Dateiupload habe ich als ein Beispiel die jetzigen Gutscheinhuelle beigefügt.
MfG

```html
<!DOCTYPE html>
<html lang="de">
<head>
<meta charset="utf-8">
<title>Gutschein-Hülle – Innenseite</title>
<link rel="stylesheet" href="https://fonts.googleapis.com/css2?family=Lobster&display=swap">
<style>
  :root {
    --burgundy: #560000;
    --burgundy-fold: #4d0000;
    --cream: #ebdd84;
    --fold-line: #e6b56a;
    --pocket-white: #ffffff;
    --pocket-rose: #d7a3a3;
  }
  html, body {
    margin: 0;
    padding: 0;
    width: 1200px;
    height: 600px;
    overflow: hidden;
    background: var(--burgundy);
  }
  .spread {
    position: relative;
    width: 1200px;
    height: 600px;
    background: var(--burgundy);
    overflow: hidden;
  }
  .band {
    position: absolute;
    left: 0;
    width: 1200px;
    height: 16px;
    background: var(--cream);
  }
  .band--top { top: 37px; }
  .band--bottom { top: 556px; }
  .fold {
    position: absolute;
    left: 601px;
    top: 0;
    width: 2px;
    height: 600px;
    background: var(--burgundy-fold);
  }
  .fold::before, .fold::after {
    content: "";
    position: absolute;
    left: 0;
    width: 2px;
    height: 16px;
    background: var(--fold-line);
  }
  .fold::before { top: 37px; }
  .fold::after { top: 556px; }
  .message {
    position: absolute;
    left: 0;
    top: 0;
    width: 608px;
    text-align: center;
    font-family: "Lobster", cursive;
    color: var(--cream);
  }
  .message__title {
    position: absolute;
    left: 0;
    width: 100%;
    top: 89px;
    margin: 0;
    font-weight: 400;
    font-size: 33px;
    line-height: 44px;
  }
  .message__body {
    position: absolute;
    left: 0;
    width: 100%;
    top: 135px;
    margin: 0;
    font-size: 24px;
    line-height: 35.8px;
  }
  .message__closing {
    position: absolute;
    left: 0;
    width: 100%;
    top: 327px;
    margin: 0;
    font-size: 24px;
    line-height: 36px;
  }
  .cutlery {
    position: absolute;
    left: 216px;
    top: 401px;
    width: 155px;
    height: 178px;
    border-radius: 20px;
    background: var(--cream);
  }
  .pocket {
    position: absolute;
    left: 0;
    top: 0;
  }
</style>
</head>
<body>
<main class="spread">
  <div class="band band--top"></div>
  <div class="band band--bottom"></div>

  <section class="message">
    <h1 class="message__title">Ein Gutschein</h1>
    <p class="message__body">
      kann&nbsp; für Vieles gut sein.<br>
      In unserem Fall lässt unsere<br>
      reichhaltige Karte viele Möglichkeiten offen.<br>
      Auf jeden Fall wird bestimmt&nbsp; geschlemmt,<br>
      geschmaust und genossen.
    </p>
    <p class="message__closing">Wir wünschen guten Appetit.</p>
  </section>

  <div class="cutlery" role="img" aria-label="Besteck-Illustration: Gabel, Löffel und Messer"></div>

  <svg class="pocket" width="1200" height="600" viewBox="0 0 1200 600" aria-hidden="true">
    <defs>
      <clipPath id="pocket-clip">
        <rect x="628" y="72" width="543" height="456"/>
      </clipPath>
    </defs>
    <rect class="pocket__area" x="628" y="72" width="543" height="456" fill="var(--pocket-white)"/>
    <polygon class="pocket__flap" points="628,72 1044,528 628,528" fill="var(--pocket-rose)"/>
    <g clip-path="url(#pocket-clip)">
      <circle class="pocket__notch-top" cx="893" cy="49" r="85" fill="var(--burgundy)"/>
      <circle class="pocket__notch-bottom" cx="890" cy="553" r="85" fill="var(--burgundy)"/>
    </g>
  </svg>

  <div class="fold"></div>
</main>
</body>
</html>
```